Net Clarity Partners Needs a New Business Card Design

Attached is my new logo that ArtFlockly created and picture of me for the back of the business card. Also attached is the information to include on the business card (on my existing business card design - NCP1 file attached).

The designer also provided a treatment of my logo that I really like if you can use it somehow. Also attached - file name "Preferred Version of New Logo."

Marla Quinteros

Net Clarity Partners
4817 Brindle Ave., #315
Houston, TX 77056

Tel: (832) 555-0147
www.netclaritypartners.example
marla@netclaritypartners.example

Thank you.

Target Market(s)

attorneys and law firms

Industry/Entity Type

Legal

Contact Information for Business Card

Proved in the Project Description

Font styles to use
Other font styles liked:
• I am open on font - no script though.

Colors
2d73b3
33a6d7

Requirements
Must have
• my logo
• company name & contact info
• my picture on the back
• colors that coordinate with the logo
Nice to have
• love to use the treated version of the logo if possible

```html
<!DOCTYPE html>
<html lang="en">
<head>
<meta charset="utf-8">
<title>Net Clarity Partners – Business Card</title>
<link rel="stylesheet" href="https://fonts.googleapis.com/css2?family=Montserrat:wght@700&family=Lato:wght@400&display=swap">
<style>
  :root {
    --brand-sky: #29a8e0;
    --brand-blue: #2d73b3;
    --ink: #1e1e1e;
    --muted: #555555;
    --rule: #2a2a2a;
    --paper: #ffffff;
    --backdrop: #d4d4d4;
    --photo-dark: #4a4442;
    --photo-warm: #b08a6e;
  }
  * { box-sizing: border-box; margin: 0; padding: 0; }
  html, body { width: 1200px; height: 1200px; overflow: hidden; }
  body {
    background: var(--backdrop);
    font-family: "Lato", sans-serif;
    position: relative;
  }
  .card {
    position: absolute;
    top: 445px;
    width: 540px;
    height: 309px;
    overflow: hidden;
  }
  .card-front { left: 40px; background: var(--brand-sky); }
  .card-back { left: 620px; background: var(--paper); }

  .wordmark {
    font-family: "Montserrat", sans-serif;
    font-weight: 700;
    white-space: nowrap;
  }
  .front-lockup {
    position: absolute;
    left: 0; right: 0; top: 128px;
    text-align: center;
    color: var(--paper);
  }
  .front-lockup .wordmark { font-size: 29px; letter-spacing: 0.5px; }
  .tagline {
    font-family: "Montserrat", sans-serif;
    font-weight: 700;
    text-transform: uppercase;
    white-space: nowrap;
  }
  .front-lockup .tagline { font-size: 9.5px; letter-spacing: 5.2px; margin-top: 4px; }

  .holder-name {
    position: absolute;
    left: 62px; top: 38px;
    font-size: 24px;
    color: var(--ink);
    letter-spacing: 0.3px;
  }
  .holder-name .initial { color: var(--brand-sky); }

  .portrait {
    position: absolute;
    left: 48px; top: 78px;
    width: 168px; height: 168px;
    border-radius: 50%;
    background: radial-gradient(circle at 55% 45%, var(--photo-warm) 0%, #8a6a55 35%, var(--photo-dark) 75%);
  }

  .frame-lines { position: absolute; left: 0; top: 0; }

  .back-lockup {
    position: absolute;
    left: 277px; top: 72px;
    width: 220px;
  }
  .back-lockup .wordmark { font-size: 16.5px; color: var(--brand-sky); }
  .back-lockup .tagline { font-size: 6px; letter-spacing: 3.05px; color: var(--muted); margin-top: 2px; }

  .contact-item {
    position: absolute;
    left: 277px;
    display: flex;
    align-items: flex-start;
    gap: 6px;
    font-size: 10.5px;
    line-height: 13px;
    color: var(--ink);
  }
  .contact-item svg { flex: none; }
  .contact-address { top: 116px; }
  .contact-phone { top: 176px; }
  .contact-email { top: 194px; }
  .contact-web { top: 221px; }
</style>
</head>
<body>

<section class="card card-front" aria-label="Business card front">
  <div class="front-lockup">
    <div class="wordmark">NET CLARITY PARTNERS</div>
    <div class="tagline">Smart Marketing for Law Firms</div>
  </div>
</section>

<section class="card card-back" aria-label="Business card back">
  <div class="holder-name">Marla <span class="initial">Q</span>uinteros</div>

  <div class="portrait" role="img" aria-label="Portrait photo of Marla Quinteros"></div>

  <svg class="frame-lines" width="540" height="309" viewBox="0 0 540 309" aria-hidden="true">
    <g fill="none" stroke="var(--rule)" stroke-width="1.2">
      <polyline points="222,52 247,52 247,256 432,256 432,275"/>
      <line x1="247" y1="82" x2="256" y2="82"/>
      <line x1="247" y1="124" x2="256" y2="124"/>
      <line x1="247" y1="180" x2="256" y2="180"/>
      <line x1="247" y1="200" x2="256" y2="200"/>
      <line x1="247" y1="226" x2="256" y2="226"/>
    </g>
  </svg>

  <div class="back-lockup">
    <div class="wordmark">NET CLARITY PARTNERS</div>
    <div class="tagline">Smart Marketing for Law Firms</div>
  </div>

  <div class="contact-item contact-address">
    <svg width="14" height="18" viewBox="0 0 14 18" aria-hidden="true">
      <path d="M7 1a6 6 0 0 0-6 6c0 4.5 6 10 6 10s6-5.5 6-10a6 6 0 0 0-6-6z" fill="none" stroke="#777" stroke-width="1.4"/>
      <circle cx="7" cy="7" r="2.2" fill="#777"/>
    </svg>
    <div>Net Clarity Partners<br>4817 Brindle Ave., #315<br>Houston, TX 77056</div>
  </div>

  <div class="contact-item contact-phone">
    <svg width="14" height="13" viewBox="0 0 14 13" aria-hidden="true">
      <path d="M3 1l2.4 2.6-1.4 1.6c.8 1.6 2 2.8 3.6 3.6l1.6-1.4L11.8 10 10.3 12C5.6 11.5 1.6 7.4 1 2.7z" fill="none" stroke="#777" stroke-width="1.2"/>
    </svg>
    <div>(832) 555-0147</div>
  </div>

  <div class="contact-item contact-email">
    <svg width="14" height="11" viewBox="0 0 14 11" aria-hidden="true">
      <rect x="1" y="1" width="12" height="9" fill="none" stroke="#777" stroke-width="1.2"/>
      <polyline points="1,1 7,6 13,1" fill="none" stroke="#777" stroke-width="1.2"/>
    </svg>
    <div>marla@netclaritypartners.example</div>
  </div>

  <div class="contact-item contact-web">
    <svg width="16" height="14" viewBox="0 0 16 14" aria-hidden="true">
      <g fill="none" stroke="#777" stroke-width="1.1">
        <circle cx="8" cy="7" r="6"/>
        <ellipse cx="8" cy="7" rx="2.6" ry="6"/>
        <line x1="2" y1="7" x2="14" y2="7"/>
      </g>
    </svg>
    <div>www.netclaritypartners.example</div>
  </div>
</section>

</body>
</html>
```